Calder Wave Banner Design for Conference

Design for a vertical retractable banner. Requirements are :
1. Use the attached PDF that shows the text content, logos and rough layout.
2. Use the logos in the attached AI files
3. Use the attached FrameVault image in the design
4. Included the design for one of our existing flyers in case useful
5. Use the corporate colours (Red and Black)
6. Design dimensions : 2000mm high x 820mm wide
7. 300 DPI

To meet a printing deadline I need the designs completed very quickly - 2 days (by COB Tuesday 29th August)

Colors
ec1f27

Requirements
Must have
• Design dimensions : 2000mm high x 820mm wide

```html
<!DOCTYPE html>
<html lang="en">
<head>
<meta charset="utf-8">
<title>Calder Wave – Conference Banner</title>
<link rel="stylesheet" href="https://fonts.googleapis.com/css2?family=Montserrat:wght@700&family=Roboto+Condensed:wght@400;700&display=swap">
<style>
  :root {
    --brand-red: #ec1f27;
    --deep-red: #b3161c;
    --ink: #050505;
    --charcoal: #1c1f24;
    --white: #ffffff;
    --cream: #f7e9c4;
    --glow: #ffb347;
    --steel-blue: #2d4f80;
    --sky-blue: #7d9cc4;
    --backdrop: #d9d9d9;
  }
  html, body {
    margin: 0;
    padding: 0;
    width: 1200px;
    height: 1200px;
    overflow: hidden;
    background: var(--backdrop);
  }
  .canvas {
    position: relative;
    width: 1200px;
    height: 1200px;
  }
  .banner {
    position: absolute;
    left: 366px;
    top: 30px;
    width: 467px;
    height: 1140px;
    background: linear-gradient(to bottom, var(--ink) 0%, var(--charcoal) 26%, var(--ink) 58%, var(--ink) 100%);
    overflow: hidden;
  }
  .brand-mark {
    position: absolute;
    left: 181px;
    top: 60px;
    width: 116px;
    height: 116px;
    border-radius: 5px;
    background: var(--brand-red);
  }
  .brand-name {
    position: absolute;
    left: 0;
    width: 100%;
    top: 206px;
    margin: 0;
    text-align: center;
    font-family: "Montserrat", sans-serif;
    font-weight: 700;
    font-size: 46px;
    line-height: 52px;
    letter-spacing: 1px;
    color: var(--white);
  }
  .brand-tagline {
    position: absolute;
    left: 0;
    width: 100%;
    top: 297px;
    margin: 0;
    text-align: center;
    font-family: "Roboto Condensed", sans-serif;
    font-weight: 400;
    font-size: 22px;
    line-height: 26px;
    color: var(--white);
    z-index: 2;
  }
  .hero-photo {
    position: absolute;
    left: 0;
    top: 330px;
    width: 100%;
    height: 337px;
    background:
      linear-gradient(to bottom, var(--charcoal) 0%, rgba(28,31,36,0) 22%),
      radial-gradient(circle at 74% 38%, #4f8fe0 0%, rgba(79,143,224,0) 30%),
      linear-gradient(100deg, var(--sky-blue) 0%, var(--steel-blue) 40%, #3b5f95 70%, var(--sky-blue) 100%);
  }
  .service-list {
    position: absolute;
    left: 0;
    top: 684px;
    margin: 0;
    padding: 0;
    list-style: none;
    font-family: "Roboto Condensed", sans-serif;
    font-weight: 400;
    font-size: 29px;
    line-height: 34px;
    color: var(--white);
  }
  .service-item {
    position: relative;
    padding-left: 80px;
    margin-bottom: 35px;
  }
  .service-item .tick {
    position: absolute;
    left: 36px;
    top: 4px;
    width: 30px;
    height: 30px;
  }
  .motto-band {
    position: absolute;
    left: 0;
    top: 931px;
    width: 100%;
    height: 148px;
    background: linear-gradient(to bottom, var(--brand-red) 0%, var(--deep-red) 25%, #4a0e0c 70%, var(--ink) 100%);
  }
  .glow-line {
    position: absolute;
    left: 0;
    width: 100%;
    height: 2px;
    background: radial-gradient(ellipse at center, #fff6d8 0%, var(--glow) 12%, rgba(255,120,40,0.5) 35%, rgba(255,120,40,0) 75%);
  }
  .glow-line.top { top: -3px; height: 4px; }
  .glow-line.bottom { bottom: -2px; }
  .motto {
    position: absolute;
    left: 0;
    top: 22px;
    margin: 0;
    font-family: "Roboto Condensed", sans-serif;
    font-weight: 700;
    font-size: 48px;
    line-height: 50px;
    color: var(--cream);
  }
  .motto span { display: block; }
  .motto .line-one { padding-left: 64px; }
  .motto .line-two { padding-left: 118px; }
</style>
</head>
<body>
  <main class="canvas">
    <section class="banner">
      <div class="brand-mark"></div>
      <h1 class="brand-name">CALDER WAVE</h1>
      <p class="brand-tagline">SOFTWARE SOLUTION DESIGN AND DEVELOPMENT</p>

      <div class="hero-photo" role="img" aria-label="Stock photo of a businessman touching a glowing code hexagon among hexagons labelled Web, Languages, Coding, Technology, Application and Development"></div>

      <ul class="service-list">
        <li class="service-item">
          <svg class="tick" viewBox="0 0 30 30" aria-hidden="true"><path d="M2 17 L11 27 L28 3 L11 20 Z" fill="var(--brand-red)"/></svg>
          CUSTOM BUSINESS SOLUTIONS
        </li>
        <li class="service-item">
          <svg class="tick" viewBox="0 0 30 30" aria-hidden="true"><path d="M2 17 L11 27 L28 3 L11 20 Z" fill="var(--brand-red)"/></svg>
          SYSTEMS INTEGRATION
        </li>
        <li class="service-item">
          <svg class="tick" viewBox="0 0 30 30" aria-hidden="true"><path d="M2 17 L11 27 L28 3 L11 20 Z" fill="var(--brand-red)"/></svg>
          SOFTWARE DEVELOPMENT<br>LIFECYCLE AUTOMATION
        </li>
      </ul>

      <div class="motto-band">
        <div class="glow-line top"></div>
        <p class="motto">
          <span class="line-one">“Your Intellect,</span>
          <span class="line-two">Our Solutions”</span>
        </p>
        <div class="glow-line bottom"></div>
      </div>
    </section>
  </main>
</body>
</html>
```